Brennock Metal recycling, a business card/logo for our industrial family metal recycling company

A new business card design/logo for our long established family metal recycling company.
I have a logo for our property company which was designed a few months ago on pixel forum which I would like to be very close to this design but have a more industrial feel to it and in a darker blue colour, please see attachments.

Target Market(s)

industries that produce metal waste for recycling, construction sites, engineering companies, manufactures, builders, plumbers, electricians, general house holders.

Industry/Entity Type

Recycling

Contact Information for Business Card

owner/director...Gordon brennock
e-mail....info@brennockscrapworks.example.co.uk
web address.....brennockscrapworks.example.co.uk

Font styles to use
Serif
Sans Serif

Colors
0255a3
ffffff

Requirements
Must have
• -dark blue business card on front.
-white on the back, see contact details, e-mail address for metal company.
-to have an industrial feel to it.
-brennock logo as business card attached but (brennock metal recycling)
please remove the little roof/arrow above brennock as this was relevant to property company.
Nice to have
• please see our website brennockscrapworks.example.co.uk with all details
being correct however I would like to refresh the logo to more like the brennock property investment business card logo attached.
Should not have
• should not contain details from property investments card as this design is for the metal recycling company.

```html
<!DOCTYPE html>
<html lang="en">
<head>
<meta charset="utf-8">
<title>Brennock Metal Recycling – Business Card</title>
<link href="https://fonts.googleapis.com/css2?family=Arimo:wght@400;700&display=swap" rel="stylesheet">
<style>
  :root {
    --brand-blue: #24367e;
    --wordmark-light: #e4e8f6;
    --ink: #2b2b2b;
    --rule-grey: #9a9a9a;
    --band-grey: #575757;
    --paper: #ffffff;
    --backdrop: #e6e7ea;
    --card-w: 780px;
    --card-h: 446px;
  }
  * { box-sizing: border-box; margin: 0; padding: 0; }
  html, body {
    width: 1200px; height: 1015px; overflow: hidden;
    background: var(--backdrop);
    font-family: "Arimo", Arial, sans-serif;
  }
  .sheet {
    width: 1200px; height: 1015px;
    display: flex; flex-direction: column; align-items: center; justify-content: center;
    gap: 40px;
  }
  .card {
    position: relative;
    width: var(--card-w); height: var(--card-h);
    box-shadow: 0 6px 18px rgba(0,0,0,.18);
    overflow: hidden;
  }

  /* Wordmark: one colour, one weight, plain square beside */
  .wordmark {
    display: flex; align-items: center;
    font-weight: 400; line-height: 1;
  }
  .wordmark__square { flex: none; }
  .wordmark__text { display: flex; flex-direction: column; }
  .wordmark__name { text-transform: uppercase; letter-spacing: .08em; }
  .wordmark__trade { text-transform: uppercase; }

  /* Front */
  .card--front {
    background: var(--brand-blue);
    display: flex; align-items: center; justify-content: center;
  }
  .card--front .wordmark { color: var(--wordmark-light); gap: 26px; }
  .card--front .wordmark__square { width: 86px; height: 86px; background: var(--wordmark-light); }
  .card--front .wordmark__name { font-size: 74px; }
  .card--front .wordmark__trade { font-size: 23px; letter-spacing: .52em; margin-top: 14px; }

  /* Back */
  .card--back { background: var(--paper); }
  .card--back .wordmark {
    position: absolute; left: 40px; top: 178px;
    color: var(--brand-blue); gap: 14px;
  }
  .card--back .wordmark__square { width: 50px; height: 50px; background: var(--brand-blue); }
  .card--back .wordmark__name { font-size: 41px; }
  .card--back .wordmark__trade { font-size: 13px; letter-spacing: .5em; margin-top: 8px; }

  .divider {
    position: absolute; left: 372px; top: 120px;
    width: 1.5px; height: 190px; background: var(--rule-grey);
  }
  .contact { position: absolute; left: 398px; top: 128px; color: var(--ink); }
  .contact__name { color: var(--brand-blue); font-weight: 700; font-size: 22px; letter-spacing: .01em; }
  .contact__role { font-size: 17px; margin-top: 2px; }
  .contact__list { list-style: none; margin-top: 24px; }
  .contact__item { display: flex; align-items: center; gap: 10px; font-size: 16px; line-height: 25px; }
  .contact__item svg { width: 16px; height: 16px; flex: none; fill: var(--brand-blue); }
  .accent { color: var(--brand-blue); }
  .band-blue { position: absolute; left: 0; bottom: 0; width: 452px; height: 20px; background: var(--brand-blue); }
  .band-grey { position: absolute; right: 0; bottom: 0; width: 318px; height: 44px; background: var(--band-grey); }
</style>
</head>
<body>
<main class="sheet">
  <section class="card card--front" aria-label="Card front">
    <div class="wordmark">
      <span class="wordmark__square" aria-hidden="true"></span>
      <p class="wordmark__text">
        <span class="wordmark__name">Brennock</span>
        <span class="wordmark__trade">Metal recycling</span>
      </p>
    </div>
  </section>

  <section class="card card--back" aria-label="Card back">
    <div class="wordmark">
      <span class="wordmark__square" aria-hidden="true"></span>
      <p class="wordmark__text">
        <span class="wordmark__name">Brennock</span>
        <span class="wordmark__trade">Metal recycling</span>
      </p>
    </div>
    <div class="divider"></div>
    <div class="contact">
      <h1 class="contact__name">GORDON BRENNOCK</h1>
      <p class="contact__role">Owner-Director</p>
      <ul class="contact__list">
        <li class="contact__item">
          <svg viewBox="0 0 16 16" aria-hidden="true"><path d="M1 6c0-2 3-3 7-3s7 1 7 3v1h-3V5.5c-1-.4-2.5-.6-4-.6s-3 .2-4 .6V7H1zM4 8h8l2 5H2zm4 1.5a1.7 1.7 0 1 0 0 3.4 1.7 1.7 0 0 0 0-3.4z"/></svg>
          07700900461
        </li>
        <li class="contact__item">
          <svg viewBox="0 0 16 16" aria-hidden="true"><path d="M4 1h8a1 1 0 0 1 1 1v12a1 1 0 0 1-1 1H4a1 1 0 0 1-1-1V2a1 1 0 0 1 1-1zm.8 1.6v9.6h6.4V2.6zM8 12.8a.8.8 0 1 0 0 1.6.8.8 0 0 0 0-1.6z"/></svg>
          020 - 7946 - 0321
        </li>
        <li class="contact__item">
          <svg viewBox="0 0 16 16" aria-hidden="true"><path d="M1 3h14v10H1zm1.6 1.5L8 8.6l5.4-4.1zm-.1 1.8v5.2l3.4-2.6zm11 0-3.4 2.6 3.4 2.6zM7 9.4l-3.6 2.7h9.2L9 9.4 8 10.1z"/></svg>
          info@brennockscrapworks.example.co.uk
        </li>
        <li class="contact__item">
          <svg viewBox="0 0 16 16" aria-hidden="true"><path d="M8 1a7 7 0 1 0 0 14A7 7 0 0 0 8 1zm-1 2.2c-.6 1-1 2-1 3h-2.8A5 5 0 0 1 7 3.2zm2 0a5 5 0 0 1 3.8 3H10c0-1-.4-2-1-3zM3.2 8H6c0 1 .4 2 1 3A5 5 0 0 1 3.2 8zm6.8 0h2.8A5 5 0 0 1 9 11c.6-1 1-2 1-3z"/></svg>
          <span>www.<span class="accent">brennockscrapworks.example.co.uk</span></span>
        </li>
      </ul>
    </div>
    <div class="band-blue"></div>
    <div class="band-grey"></div>
  </section>
</main>
</body>
</html>
```